Startup Drone Platform Company business card

We are needing a business card design for our employees. We are a startup drone platform. We are looking for a business card that has our logo on one side, with the employee/company details on the opposite side. We are looking for something that is very eye catching, modern, and bold.

Target Market(s)

This will target both drone pilots and drone businesses, along with all the industries that could utilize drone services (aerial video, aerial photos, inspections, 3d mapping, etc).

Industry/Entity Type

Business

```html
<!DOCTYPE html>
<html lang="en">
<head>
<meta charset="utf-8">
<title>AeroHire Business Card</title>
<link href="https://fonts.googleapis.com/css2?family=Montserrat:wght@400;500;600&display=swap" rel="stylesheet">
<style>
  :root{
    --stage:#2b2b2d;
    --card:#050505;
    --teal:#2fbfc9;
    --white:#ffffff;
    --muted:#d9d9d9;
  }
  *{box-sizing:border-box;margin:0;padding:0}
  html,body{width:1200px;height:900px;overflow:hidden}
  body{background:var(--stage);font-family:"Montserrat",sans-serif;color:var(--white);position:relative}
  .card{position:absolute;width:500px;height:286px;background:var(--card);border-radius:16px;overflow:hidden;box-shadow:0 14px 30px rgba(0,0,0,.45)}
  .card-logo-side{left:90px;top:150px}
  .card-details-side{left:610px;top:470px}
  .card-shapes{position:absolute;inset:0}

  .brand-mark{position:absolute;left:0;right:0;top:112px;display:flex;align-items:center;justify-content:center;gap:14px}
  .brand-dot{width:18px;height:18px;border-radius:50%;background:var(--teal)}
  .brand-name{font-weight:500;font-size:26px;letter-spacing:.32em;color:var(--white)}

  .website-tab{position:absolute;left:18px;top:256px;font-size:11px;font-weight:400;letter-spacing:.02em}
  .website-tab strong{font-weight:600}

  .wordmark{position:absolute;left:0;right:0;top:62px;display:flex;align-items:center;justify-content:center;gap:16px}
  .wordmark .brand-name{font-size:30px;letter-spacing:.5em}
  .wordmark .brand-dot{width:20px;height:20px}

  .holder{position:absolute;right:24px;top:128px;text-align:right}
  .holder-name{font-size:22px;font-weight:600;color:var(--teal);line-height:1}
  .holder-role{font-size:11px;color:var(--white);margin-top:4px}
  .holder-rule{position:absolute;right:20px;top:172px;width:300px;height:1px;background:var(--muted)}

  .address-rule{position:absolute;left:26px;top:180px;width:150px;height:1px;background:var(--muted)}
  .address{position:absolute;left:26px;top:188px;font-size:12px;line-height:1.35}
  .contacts{position:absolute;left:26px;top:224px;list-style:none;font-size:12px;line-height:1.4}
  .contacts li{display:flex;align-items:center;gap:8px}
  .contacts svg{width:10px;height:10px;flex:none}
  .contacts .accent{color:var(--teal);font-weight:600}
</style>
</head>
<body>

<section class="card card-logo-side" aria-label="Card front">
  <svg class="card-shapes" viewBox="0 0 500 286" aria-hidden="true">
    <rect x="232" y="272" width="268" height="14" fill="var(--white)"/>
    <polygon points="0,244 206,244 236,266 236,286 0,286" fill="var(--teal)"/>
  </svg>
  <div class="brand-mark">
    <span class="brand-dot"></span>
    <span class="brand-name">AEROHIRE</span>
  </div>
  <p class="website-tab">www.<strong>AEROHIRE</strong>.com</p>
</section>

<section class="card card-details-side" aria-label="Card back">
  <svg class="card-shapes" viewBox="0 0 500 286" aria-hidden="true">
    <rect x="0" y="274" width="330" height="12" fill="var(--white)"/>
    <polygon points="338,226 500,226 500,286 318,286 318,262" fill="var(--teal)"/>
  </svg>
  <div class="wordmark">
    <span class="brand-dot"></span>
    <span class="brand-name">AEROHIRE</span>
  </div>
  <div class="holder">
    <p class="holder-name">Marcus Reyel</p>
    <p class="holder-role">Director</p>
  </div>
  <div class="holder-rule"></div>
  <div class="address-rule"></div>
  <p class="address">48 Foundry Lane<br>Millbrook, NY 12345</p>
  <ul class="contacts">
    <li><svg viewBox="0 0 10 10"><path d="M2 0.8 L3.6 2.8 L2.8 4 Q4 6.2 6 7.2 L7.2 6.4 L9.2 8 L8 9.4 Q3 8.6 0.6 2 Z" fill="var(--teal)"/></svg>+330 5550-1942</li>
    <li><svg viewBox="0 0 10 10"><rect x="0.7" y="2" width="8.6" height="6" fill="none" stroke="var(--teal)" stroke-width="1"/><path d="M0.7 2 L5 5.4 L9.3 2" fill="none" stroke="var(--teal)" stroke-width="1"/></svg>info@aerohire.com</li>
    <li><svg viewBox="0 0 10 10"><circle cx="5" cy="5" r="4.3" fill="none" stroke="var(--teal)" stroke-width="1"/><ellipse cx="5" cy="5" rx="1.8" ry="4.3" fill="none" stroke="var(--teal)" stroke-width=".8"/><line x1=".7" y1="5" x2="9.3" y2="5" stroke="var(--teal)" stroke-width=".8"/></svg>www.<span class="accent">AEROHIRE</span>.com</li>
  </ul>
</section>

</body>
</html>
```